Wow me with your Earring card options!

An A7 portrait sized earring card is required for Marble & Mango. Inspired by Marble and fueled by Mango we love our accessories to do the talking. Bold statement earrings are our thing. Our earring cards need to showcase our brand while not stealing all of the limelight from the earrings themselves. Earring care information needs to be included on the back side of the card. Our simple logo needs to be the basis for the colour choices used on the card.

Requirements
Should not have
• No florals please 😊

```html
<!DOCTYPE html>
<html lang="en">
<head>
<meta charset="utf-8">
<title>Marble &amp; Mango – Earring Card</title>
<link href="https://fonts.googleapis.com/css2?family=EB+Garamond:wght@400;600&display=swap" rel="stylesheet">
<style>
  :root {
    --backdrop: #fdf7d8;
    --ink: #1a1a1a;
    --card-black: #0a0a0c;
    --logo-dark: #3b3554;
    --logo-light: #c9c9cc;
    --grad-purple: #9d92c6;
    --grad-pink: #d8a2aa;
    --grad-orange: #f3a882;
    --grad-yellow: #f6eaa2;
    --grad-green: #a8d190;
    --grad-teal: #78b0b3;
    --social-tile: #2b2840;
  }
  * { box-sizing: border-box; margin: 0; padding: 0; }
  html, body { width: 1200px; height: 1200px; overflow: hidden; }
  body {
    background: var(--backdrop);
    position: relative;
    font-family: "EB Garamond", Garamond, serif;
    color: var(--ink);
  }
  .card { position: absolute; top: 229px; }
  .card-back {
    left: 70px; width: 521px; height: 731px;
    background: linear-gradient(180deg,
      var(--grad-purple) 0%, var(--grad-pink) 28%, var(--grad-orange) 40%,
      var(--grad-yellow) 57%, var(--grad-green) 78%, var(--grad-teal) 100%);
  }
  .card-front {
    left: 612px; width: 518px; height: 726px;
    background: var(--card-black);
  }
  .brand-name {
    position: absolute; left: 0; right: 0;
    text-align: center;
    font-weight: 600; font-size: 58px; line-height: 1.05;
    letter-spacing: 1px;
  }
  .card-back .brand-name { top: 92px; color: var(--logo-dark); }
  .card-front .brand-name { top: 288px; color: var(--logo-light); }

  .care-list { position: absolute; left: 62px; top: 270px; list-style: none; }
  .care-item {
    display: flex; align-items: center; height: 36.5px;
    font-size: 20.5px;
  }
  .care-icon { width: 30px; height: 28px; margin-right: 22px; flex: none; }

  .contact-box {
    position: absolute; left: 72px; top: 442px; width: 377px; height: 131px;
    border: 1.6px solid var(--ink); border-radius: 14px;
    padding: 16px 0 0 28px;
  }
  .contact-row {
    display: flex; align-items: center; height: 35px;
    font-size: 18.5px;
  }
  .contact-icon { width: 26px; height: 26px; margin-right: 22px; flex: none; }

  .social-row { position: absolute; left: 134px; top: 609px; display: flex; gap: 25px; }
  .social-tile {
    width: 44px; height: 44px; border-radius: 5px; background: var(--social-tile);
  }
</style>
</head>
<body>

<section class="card card-back" aria-label="Earring card back with care information">
  <div class="brand-name">Marble<br>&amp; Mango</div>

  <ul class="care-list">
    <li class="care-item">
      <svg class="care-icon" viewBox="0 0 30 28" fill="none" stroke="#1a1a1a" stroke-width="1.1">
        <path d="M11 6 C7 13 5 16 5 19 a6 6 0 0 0 12 0 c0-3-2-6-6-13z"/>
        <path d="M21 2 C19 6 18 7 18 9 a3 3 0 0 0 6 0 c0-2-1-3-3-7z"/>
      </svg>
      Avoid moisture &amp; remove before bathing
    </li>
    <li class="care-item">
      <svg class="care-icon" viewBox="0 0 30 28" fill="none" stroke="#1a1a1a" stroke-width="1.1">
        <rect x="5" y="5" width="20" height="8" rx="2"/>
        <rect x="3" y="12" width="24" height="7" rx="1"/>
        <path d="M5 19v3M25 19v3M8 9h5M17 9h5"/>
      </svg>
      For comforts sake, remove before bed!
    </li>
    <li class="care-item">
      <svg class="care-icon" viewBox="0 0 30 28" fill="none" stroke="#1a1a1a" stroke-width="1.1">
        <rect x="11" y="2" width="6" height="5"/>
        <path d="M17 4h6M23 3a2 2 0 1 1 0 2"/>
        <path d="M11 9h6l4 5v9a3 3 0 0 1-3 3h-8a3 3 0 0 1-3-3v-9z"/>
      </svg>
      Avoid contact with perfume &amp; lotions
    </li>
    <li class="care-item">
      <svg class="care-icon" viewBox="0 0 30 28" fill="none" stroke="#1a1a1a" stroke-width="1.1">
        <circle cx="15" cy="14" r="6"/>
        <path d="M15 2v4M15 22v4M3 14h4M23 14h4M6.5 5.5l3 3M20.5 19.5l3 3M6.5 22.5l3-3M20.5 8.5l3-3"/>
      </svg>
      Store away from direct sunlight
    </li>
  </ul>

  <div class="contact-box">
    <div class="contact-row">
      <svg class="contact-icon" viewBox="0 0 26 26" fill="none" stroke="#1a1a1a" stroke-width="1.1">
        <circle cx="13" cy="13" r="11"/>
        <ellipse cx="13" cy="13" rx="5" ry="11"/>
        <path d="M2 13h22M4 7h18M4 19h18M13 2v22"/>
      </svg>
      www.marbleandmango.com.au
    </div>
    <div class="contact-row">
      <svg class="contact-icon" viewBox="0 0 26 26" fill="none" stroke="#1a1a1a" stroke-width="1.1">
        <rect x="2" y="9" width="22" height="14"/>
        <path d="M2 9l11 8 11-8M2 23l8-7M24 23l-8-7"/>
        <circle cx="13" cy="6" r="3"/>
      </svg>
      hello@marbleandmango.com.au
    </div>
    <div class="contact-row">
      <svg class="contact-icon" viewBox="0 0 26 26" fill="none" stroke="#1a1a1a" stroke-width="1.1">
        <circle cx="13" cy="13" r="11.5"/>
        <circle cx="13" cy="10" r="4"/>
        <path d="M5.5 21.5c2-4 4.5-5.5 7.5-5.5s5.5 1.5 7.5 5.5"/>
      </svg>
      @marbleandmango
    </div>
  </div>

  <div class="social-row" aria-label="Social media links">
    <div class="social-tile"></div>
    <div class="social-tile"></div>
    <div class="social-tile"></div>
    <div class="social-tile"></div>
  </div>
</section>

<section class="card card-front" aria-label="Earring card front">
  <div class="brand-name">Marble<br>&amp; Mango</div>
</section>

</body>
</html>
```